" A Voltrana é uma empresa cuja especialidade é atuar diretamente no setor de energia, oferecendo a seus clientes gestão de energia e utilidades (água, gás, vapor, ar comprimido) com o objetivo principal de obter informações, padrões e variáveis de consumo e também eficiência energética para agir de forma assertiva no foco do desperdício e na otimização da utilização dos recursos em um parque industrial ou edifício. "

```html
<!DOCTYPE html>
<html lang="pt-BR">
<head>
<meta charset="UTF-8">
<title>Voltrana – Cartão de visita</title>
<link rel="stylesheet" href="https://fonts.googleapis.com/css2?family=Montserrat:wght@500;600;800&display=swap">
<style>
  :root {
    --yellow: #f2b705;
    --yellow-deep: #e8a50a;
    --green: #1f9a3e;
    --green-deep: #167a30;
    --ink: #4a4a4a;
    --card: #ffffff;
    --backdrop: #ecebe8;
  }
  * { margin: 0; padding: 0; box-sizing: border-box; }
  html, body { width: 1200px; height: 1200px; overflow: hidden; }
  body {
    background: var(--backdrop);
    font-family: "Montserrat", sans-serif;
    display: flex;
    flex-direction: column;
    align-items: center;
    justify-content: center;
    gap: 70px;
  }
  .card {
    position: relative;
    width: 840px;
    height: 480px;
    background: var(--card);
    overflow: hidden;
    box-shadow: 0 10px 30px rgba(0,0,0,0.12);
  }
  .brand { display: flex; align-items: center; gap: 16px; }
  .brand-dot {
    width: 26px; height: 26px; border-radius: 50%;
    background: var(--yellow);
  }
  .brand-name {
    font-weight: 800;
    color: var(--yellow-deep);
    letter-spacing: 0.04em;
    text-transform: uppercase;
    line-height: 1;
  }
  .brand-tagline {
    font-weight: 600;
    color: var(--green);
    letter-spacing: 0.05em;
    margin-top: 6px;
  }
  /* front */
  .card-front .brand { position: absolute; top: 110px; left: 440px; }
  .card-front .brand-name { font-size: 52px; }
  .card-front .brand-tagline { font-size: 18px; }
  .band { position: absolute; height: 70px; }
  .card-front .band-yellow { left: 0; bottom: 0; width: 520px; background: var(--yellow); }
  .card-front .band-green { right: 0; bottom: 0; width: 320px; background: var(--green); }
  /* back */
  .card-back .band-yellow { left: 0; top: 0; width: 560px; height: 40px; background: var(--yellow); }
  .card-back .band-green { right: 0; top: 0; width: 280px; height: 40px; background: var(--green); }
  .card-back .brand { position: absolute; top: 210px; left: 300px; }
  .card-back .brand-name { font-size: 40px; }
  .card-back .brand-tagline { font-size: 14px; }
  .contacts {
    position: absolute; top: 320px; left: 300px;
    list-style: none;
    font-size: 15px; font-weight: 500; color: var(--ink);
  }
  .contacts li { display: flex; align-items: center; gap: 12px; margin-bottom: 10px; }
  .contact-icon {
    width: 22px; height: 22px; border-radius: 50%;
    background: var(--green-deep);
    display: flex; align-items: center; justify-content: center;
    flex-shrink: 0;
  }
  .contact-icon svg { width: 12px; height: 12px; fill: #fff; }
</style>
</head>
<body>
  <section class="card card-front" aria-label="Frente do cartão">
    <div class="brand">
      <span class="brand-dot"></span>
      <div>
        <div class="brand-name">Voltrana</div>
        <div class="brand-tagline">soluções em energia</div>
      </div>
    </div>
    <div class="band band-yellow"></div>
    <div class="band band-green"></div>
  </section>

  <section class="card card-back" aria-label="Verso do cartão">
    <div class="band band-yellow"></div>
    <div class="band band-green"></div>
    <div class="brand">
      <span class="brand-dot"></span>
      <div>
        <div class="brand-name">Voltrana</div>
        <div class="brand-tagline">soluções em energia</div>
      </div>
    </div>
    <ul class="contacts">
      <li>
        <span class="contact-icon"><svg viewBox="0 0 12 12"><path d="M6 0.5a4 4 0 0 0-4 4c0 3 4 7 4 7s4-4 4-7a4 4 0 0 0-4-4zm0 5.5a1.5 1.5 0 1 1 0-3 1.5 1.5 0 0 1 0 3z"/></svg></span>
        Rua das Turbinas, 120 – Campinas – SP
      </li>
      <li>
        <span class="contact-icon"><svg viewBox="0 0 12 12"><path d="M2.5 1l2 2-1 1.5c.7 1.5 1.8 2.6 3.3 3.3l1.5-1 2 2-1.3 1.7C5 10 2 7 .8 2.3z"/></svg></span>
        (19) 3555-0142 | (19) 98555-0187
      </li>
      <li>
        <span class="contact-icon"><svg viewBox="0 0 12 12"><path d="M1 2.5h10v7H1zm1 1v.4l4 2.6 4-2.6v-.4z"/></svg></span>
        contato@voltrana.com.br
      </li>
      <li>
        <span class="contact-icon"><svg viewBox="0 0 12 12"><path d="M6 1a5 5 0 1 0 0 10A5 5 0 0 0 6 1zm0 1.2c.6.7 1 1.7 1.1 2.8H4.9C5 3.9 5.4 2.9 6 2.2zM2.3 6.8h1.5c.1 1 .4 1.9.8 2.5a3.9 3.9 0 0 1-2.3-2.5zm0-1.6A3.9 3.9 0 0 1 4.6 2.7c-.4.7-.7 1.5-.8 2.5zm3.7 4.6c-.6-.7-1-1.8-1.1-3h2.2c-.1 1.2-.5 2.3-1.1 3zm1.4-.5c.4-.7.7-1.5.8-2.5h1.5a3.9 3.9 0 0 1-2.3 2.5zm.8-4.1c-.1-1-.4-1.8-.8-2.5a3.9 3.9 0 0 1 2.3 2.5z"/></svg></span>
        www.voltranaenergia.com.br
      </li>
    </ul>
  </section>
</body>
</html>
```